Marvane Painting Epoxy Flyer

We need a promotional flyer for a new epoxy floor coatings division of our painting company. We do epoxy garage floor coatings and paver sealing. It needs to be based on and very similar to the attached flyer. The garage floor picture needs to look more realistic, and the before and after pavers pictures should look less shiny but still a good contrast. Include attached logo

```html
<!DOCTYPE html>
<html lang="en">
<head>
<meta charset="utf-8">
<title>Marvane Painting – Garage &amp; Driveway Flyer</title>
<link href="https://fonts.googleapis.com/css2?family=Poppins:wght@400;500;600;700&display=swap" rel="stylesheet">
<style>
  :root{
    --blue:#023e94;
    --green:#3b8a10;
    --orange:#eeab2e;
    --ink:#1b1b1b;
    --white:#ffffff;
  }
  *{margin:0;padding:0;box-sizing:border-box}
  html,body{width:967px;height:1200px;overflow:hidden;background:var(--white)}
  body{font-family:'Poppins',sans-serif;color:var(--ink);position:relative}
  .hero{position:absolute;left:0;top:0;width:967px;height:530px}
  .brand{position:absolute;left:0;top:112px;width:967px;display:flex;justify-content:center;align-items:center;gap:10px}
  .brand-dot{width:22px;height:22px;border-radius:50%;background:var(--green)}
  .brand-name{font-weight:600;font-size:22px;color:var(--ink)}
  .headline{position:absolute;left:0;top:512px;width:967px;text-align:center}
  .headline-lead{font-size:54px;font-weight:400;line-height:1.1}
  .headline-main{font-size:55px;font-weight:700;color:var(--green);line-height:1.1;margin-top:-2px}
  .headline-sub{font-size:23px;font-weight:600;margin-top:6px}
  .service{position:absolute;top:688px;width:380px;height:200px;border-radius:22px;background:var(--white);padding:17px 0 0 26px}
  .service--epoxy{left:88px;border:2px solid var(--green)}
  .service--pavers{left:502px;border:2px solid var(--blue)}
  .service-title{width:326px;height:35px;border-radius:6px;color:var(--white);font-weight:600;font-size:22px;text-align:center;line-height:36px}
  .service--epoxy .service-title{background:var(--green)}
  .service--pavers .service-title{background:var(--blue)}
  .service-list{list-style:none;margin-top:9px}
  .service-list li{display:flex;align-items:center;gap:8px;font-size:15.5px;height:33.5px}
  .service-list svg{flex:none}
  .tagline-main{position:absolute;left:0;top:905px;width:967px;text-align:center;font-weight:600;font-size:22.5px;letter-spacing:-.2px}
  .badges{position:absolute;left:0;top:952px;width:967px;height:100px}
  .badge{position:absolute;top:0;width:200px;text-align:center;font-weight:500;font-size:17px;line-height:1.15}
  .badge svg{display:block;margin:0 auto 8px}
  .badge-divider{position:absolute;top:0;width:1px;height:100px;background:#cfcfcf}
  .cta{position:absolute;left:99px;top:1081px;width:362px;height:37px;border-radius:19px;background:var(--orange);color:var(--white);font-weight:600;font-size:22px;text-align:center;line-height:38px}
  .phone{position:absolute;left:474px;top:1070px;display:flex;align-items:center;gap:6px}
  .phone-number{font-weight:700;font-size:50px;letter-spacing:-.5px;line-height:1}
  .promise{position:absolute;left:0;top:1124px;width:967px;text-align:center;font-size:27px;letter-spacing:5.4px;font-weight:400}
  .footer-bar{position:absolute;left:0;top:1182px;width:967px;height:18px;background:var(--blue)}
</style>
</head>
<body>

<svg class="hero" viewBox="0 0 967 530" xmlns="http://www.w3.org/2000/svg">
  <defs>
    <linearGradient id="g-garage-before" x1="0" y1="0" x2="0" y2="1">
      <stop offset="0" stop-color="#a9c9e4"/><stop offset=".35" stop-color="#b46a63"/><stop offset=".65" stop-color="#8c6b5b"/><stop offset="1" stop-color="#7c7366"/>
    </linearGradient>
    <linearGradient id="g-garage-after" x1="0" y1="0" x2="0" y2="1">
      <stop offset="0" stop-color="#8e4f2c"/><stop offset=".6" stop-color="#9a5b34"/><stop offset="1" stop-color="#c79a78"/>
    </linearGradient>
    <linearGradient id="g-pavers-before" x1="0" y1="0" x2="0" y2="1">
      <stop offset="0" stop-color="#6aa6dc"/><stop offset=".4" stop-color="#9b8a74"/><stop offset=".7" stop-color="#7a5e44"/><stop offset="1" stop-color="#d8cbbb"/>
    </linearGradient>
    <linearGradient id="g-pavers-after" x1="0" y1="0" x2="0" y2="1">
      <stop offset="0" stop-color="#7db7e8"/><stop offset=".4" stop-color="#8b7563"/><stop offset=".7" stop-color="#c9a877"/><stop offset="1" stop-color="#b59a83"/>
    </linearGradient>
  </defs>

  <polygon points="0,0 967,0 967,240 700,240 560,474 482,510 410,474 270,240 0,240" fill="var(--blue)"/>
  <polygon points="302,0 657,0 657,159 482,256 302,159" fill="var(--white)"/>

  <g stroke="var(--white)" stroke-width="4">
    <polygon role="img" aria-label="Garage with freshly finished paver driveway, after" points="250,250 346,194 470,273 470,441 340,512 211,441" fill="url(#g-garage-after)"/>
    <polygon role="img" aria-label="Garage with worn gravel floor area, before" points="0,238 144,160 288,238 288,414 144,481 0,414" fill="url(#g-garage-before)"/>
    <polygon role="img" aria-label="Stone-faced house with dull paver driveway, before" points="497,273 641,194 720,245 720,443 641,513 497,441" fill="url(#g-pavers-before)"/>
    <polygon role="img" aria-label="Stone-faced house with sealed paver driveway, after" points="677,238 822,160 967,238 967,414 822,481 677,414" fill="url(#g-pavers-after)"/>
  </g>

  <polygon points="0,414 288,417 144,481" fill="var(--green)"/>
  <polygon points="211,441 470,441 340,512" fill="var(--orange)"/>
  <polygon points="515,443 758,443 641,513" fill="var(--green)"/>
  <polygon points="694,414 967,414 822,481" fill="var(--orange)"/>

  <g font-family="Poppins, sans-serif" font-weight="700" font-size="24" fill="var(--white)" text-anchor="middle">
    <text x="138" y="442">BEFORE</text>
    <text x="330" y="472">AFTER</text>
    <text x="634" y="473">BEFORE</text>
    <text x="823" y="443">AFTER</text>
  </g>
</svg>

<div class="brand">
  <span class="brand-dot"></span>
  <span class="brand-name">Marvane Painting</span>
</div>

<div class="headline">
  <div class="headline-lead">Upgrade Your</div>
  <div class="headline-main">Garage &amp; Driveway</div>
  <div class="headline-sub">From worn-out to like new</div>
</div>

<section class="service service--epoxy">
  <h2 class="service-title">EPOXY FLOOR COATINGS</h2>
  <ul class="service-list">
    <li><svg width="13" height="13" viewBox="0 0 13 13"><rect x=".7" y=".7" width="11.6" height="11.6" fill="none" stroke="var(--green)" stroke-width="1.3"/><path d="M3 6.5l2.3 2.3L10 3.6" fill="none" stroke="var(--green)" stroke-width="1.5"/></svg>Durable, long-lasting finish</li>
    <li><svg width="13" height="13" viewBox="0 0 13 13"><rect x=".7" y=".7" width="11.6" height="11.6" fill="none" stroke="var(--green)" stroke-width="1.3"/><path d="M3 6.5l2.3 2.3L10 3.6" fill="none" stroke="var(--green)" stroke-width="1.5"/></svg>Slip-resistant texture</li>
    <li><svg width="13" height="13" viewBox="0 0 13 13"><rect x=".7" y=".7" width="11.6" height="11.6" fill="none" stroke="var(--green)" stroke-width="1.3"/><path d="M3 6.5l2.3 2.3L10 3.6" fill="none" stroke="var(--green)" stroke-width="1.5"/></svg>Covers cracks &amp; imperfections</li>
    <li><svg width="13" height="13" viewBox="0 0 13 13"><rect x=".7" y=".7" width="11.6" height="11.6" fill="none" stroke="var(--green)" stroke-width="1.3"/><path d="M3 6.5l2.3 2.3L10 3.6" fill="none" stroke="var(--green)" stroke-width="1.5"/></svg>Easy to clean &amp; maintain</li>
  </ul>
</section>

<section class="service service--pavers">
  <h2 class="service-title">PAVER SEALING</h2>
  <ul class="service-list">
    <li><svg width="13" height="13" viewBox="0 0 13 13"><rect x=".7" y=".7" width="11.6" height="11.6" fill="none" stroke="var(--blue)" stroke-width="1.3"/><path d="M3 6.5l2.3 2.3L10 3.6" fill="none" stroke="var(--blue)" stroke-width="1.5"/></svg>Restores color &amp; enhances appearance</li>
    <li><svg width="13" height="13" viewBox="0 0 13 13"><rect x=".7" y=".7" width="11.6" height="11.6" fill="none" stroke="var(--blue)" stroke-width="1.3"/><path d="M3 6.5l2.3 2.3L10 3.6" fill="none" stroke="var(--blue)" stroke-width="1.5"/></svg>Protects from sun fading</li>
    <li><svg width="13" height="13" viewBox="0 0 13 13"><rect x=".7" y=".7" width="11.6" height="11.6" fill="none" stroke="var(--blue)" stroke-width="1.3"/><path d="M3 6.5l2.3 2.3L10 3.6" fill="none" stroke="var(--blue)" stroke-width="1.5"/></svg>Helps prevent weeds &amp; sand loss</li>
    <li><svg width="13" height="13" viewBox="0 0 13 13"><rect x=".7" y=".7" width="11.6" height="11.6" fill="none" stroke="var(--blue)" stroke-width="1.3"/><path d="M3 6.5l2.3 2.3L10 3.6" fill="none" stroke="var(--blue)" stroke-width="1.5"/></svg>Easier to clean &amp; maintain</li>
  </ul>
</section>

<div class="tagline-main">PRACTICAL UPGRADES THAT PROTECT AND IMPROVE YOUR HOME</div>

<div class="badges">
  <div class="badge" style="left:126px">
    <svg width="54" height="54" viewBox="0 0 54 54"><circle cx="27" cy="27" r="27" fill="var(--blue)"/><rect x="18" y="13" width="17" height="23" rx="1.5" fill="var(--white)"/><path d="M21 19h11M21 23h11M21 27h8M21 31h6" stroke="var(--blue)" stroke-width="1.6"/><circle cx="35" cy="36" r="5" fill="var(--white)" stroke="var(--blue)" stroke-width="1.5"/></svg>
    Licensed<br>&amp; Insured
  </div>
  <div class="badge-divider" style="left:322px"></div>
  <div class="badge" style="left:347px">
    <svg width="54" height="54" viewBox="0 0 54 54"><circle cx="27" cy="27" r="27" fill="var(--green)"/><path d="M14 20l3-6h20l3 6z" fill="var(--white)"/><rect x="15" y="22" width="24" height="16" fill="none" stroke="var(--white)" stroke-width="2"/><circle cx="22" cy="28" r="2.3" fill="var(--white)"/><circle cx="32" cy="28" r="2.3" fill="var(--white)"/><path d="M18 36c0-3 2-4.5 4-4.5s4 1.5 4 4.5M28 36c0-3 2-4.5 4-4.5s4 1.5 4 4.5" fill="var(--white)"/></svg>
    Family-Owned<br>Local Business
  </div>
  <div class="badge-divider" style="left:566px"></div>
  <div class="badge" style="left:595px">
    <svg width="54" height="54" viewBox="0 0 54 54"><circle cx="27" cy="27" r="27" fill="var(--blue)"/><path d="M27 42c-7-9-11-14-11-19a11 11 0 0 1 22 0c0 5-4 10-11 19z" fill="var(--white)"/><circle cx="27" cy="23" r="4.5" fill="var(--blue)"/></svg>
    Serving Prescott &amp;<br>Surrounding Areas
  </div>
</div>

<div class="cta">CALL FOR A FREE ESTIMATE</div>
<div class="phone">
  <svg width="40" height="40" viewBox="0 0 40 40"><circle cx="20" cy="20" r="18" fill="none" stroke="var(--green)" stroke-width="3"/><path d="M13 11c1-1 2.5-1 3.2 0l2.3 3.4c.6.9.4 2-.4 2.6l-1.4 1c1 2.6 3 4.6 5.6 5.7l1-1.4c.6-.8 1.8-1 2.6-.4l3.4 2.3c1 .7 1 2.2 0 3.2l-1.6 1.6C24 33 9 18 11.4 12.6z" fill="var(--green)"/></svg>
  <span class="phone-number">928-555-0147</span>
</div>
<div class="promise">Fast, professional service you can trust</div>

<div class="footer-bar"></div>

</body>
</html>
```